Business card design Needed for new logo / Construction business, home extensions and new builds

We need a business card design using our new logo files which i will attach to this project :)

We are a small construction business specialising in home extensions, new builds and property development. We are very ambitious and would appreciate professional and elegant designs for our new business card.

Very serious about using the services on BriefNest and recently acquired our new logo from here :)

Please get involved, i will feedback when i can as i am very busy but can respond daily, thanks

Target Market(s)

People that want to build onto their houses, new building developments or adding too their existing property

Industry/Entity Type

Construction

Contact Information for Business Card

Hollin Marsh Construction, Tobias Renwick (Managing Director), Tel 07822200444, email - info@hollin-marsh, www.hollin-marsh.co.uk

Colors

Designer to choose colors to be used in the design.

Requirements
Must have
• I like a deep grey on the back please. A lot of you have provided black from and back, try mixing things up a little. The black looks cool 😎 Thanks

```html
<!DOCTYPE html>
<html lang="en">
<head>
<meta charset="utf-8">
<title>Hollin Marsh Construction – Business Card</title>
<link href="https://fonts.googleapis.com/css2?family=Open+Sans:wght@400;600;700&display=swap" rel="stylesheet">
<style>
  :root {
    --page: #2a2a2d;
    --card-front: #1f1f22;
    --card-back: #141416;
    --gold: #e0a526;
    --gold-deep: #b97d12;
    --silver: #d9d9dc;
    --text: #f2f2f2;
    --muted: #3a3a3e;
  }
  * { box-sizing: border-box; margin: 0; padding: 0; }
  html, body { width: 1200px; height: 780px; overflow: hidden; }
  body {
    background: var(--page);
    font-family: "Open Sans", Arial, sans-serif;
    color: var(--text);
    position: relative;
  }
  .card {
    position: absolute;
    top: 235px;
    width: 540px;
    height: 310px;
    border-top: 2px solid var(--gold);
    border-left: 2px solid var(--gold);
    border-bottom: 2px solid var(--gold-deep);
    border-right: 2px solid var(--gold-deep);
    overflow: hidden;
  }
  .card--front { left: 40px; background: var(--card-front); }
  .card--back { left: 620px; background: var(--card-back); }

  .brand {
    position: absolute;
    top: 34px;
    left: 34px;
    display: flex;
    align-items: center;
    gap: 10px;
  }
  .brand__mark {
    width: 14px; height: 14px;
    background: var(--gold);
  }
  .brand__name {
    font-size: 17px;
    font-weight: 600;
    letter-spacing: 1px;
    text-transform: uppercase;
    color: var(--gold);
  }

  .contact {
    position: absolute;
    top: 82px;
    left: 34px;
    font-size: 13.5px;
    line-height: 1.45;
  }
  .contact__address { margin-bottom: 8px; }
  .contact__line { display: flex; align-items: center; gap: 8px; }
  .contact__icon { width: 12px; height: 12px; flex: none; }
  .contact__line--web { padding-left: 20px; }

  .watermark {
    position: absolute;
    right: 36px;
    bottom: 22px;
    font-size: 30px;
    font-weight: 700;
    color: var(--muted);
    letter-spacing: 1px;
    text-transform: uppercase;
    text-align: right;
    line-height: 1.1;
  }

  .person {
    position: absolute;
    right: 44px;
    top: 118px;
    text-align: right;
  }
  .person__name { font-size: 26px; font-weight: 700; letter-spacing: 0.5px; }
  .person__first { color: var(--silver); }
  .person__last { color: var(--gold); }
  .person__role { font-size: 15px; font-weight: 600; margin-top: 2px; }
  .accent-bar {
    position: absolute;
    right: 0;
    top: 112px;
    width: 14px;
    height: 78px;
    background: linear-gradient(180deg, var(--gold), var(--gold-deep));
  }

  .back-texture {
    position: absolute;
    inset: 0;
    background: linear-gradient(100deg, #141416 0%, #1c1c1f 55%, #4a4a4f 85%, #8d8d93 100%);
  }
  .back-brand {
    position: absolute;
    right: 26px;
    bottom: 20px;
    display: flex;
    align-items: center;
    gap: 6px;
    background: var(--card-back);
    padding: 4px 8px;
  }
  .back-brand__mark { width: 8px; height: 8px; background: var(--gold); }
  .back-brand__name {
    font-size: 9px;
    font-weight: 600;
    letter-spacing: 0.6px;
    text-transform: uppercase;
    color: var(--gold);
  }
</style>
</head>
<body>

<section class="card card--front">
  <div class="brand">
    <span class="brand__mark"></span>
    <span class="brand__name">Hollin Marsh Construction</span>
  </div>

  <div class="contact">
    <p class="contact__address">Fernhill Lane, Westbury<br>Ashcombe, AC4 7QT</p>
    <p class="contact__line">
      <svg class="contact__icon" viewBox="0 0 12 12"><path d="M2.5 1 L4.5 1 L5.2 3.6 L4 4.6 Q5 7 7.4 8 L8.4 6.8 L11 7.5 L11 9.5 Q10.5 11 9 11 Q1 10 1 2.5 Q1 1 2.5 1Z" fill="#e0a526"/></svg>
      0782 220 0444
    </p>
    <p class="contact__line">
      <svg class="contact__icon" viewBox="0 0 12 12"><rect x="0.5" y="2" width="11" height="8" rx="1" fill="#e0a526"/><path d="M1 2.6 L6 6.6 L11 2.6" stroke="#1f1f22" stroke-width="1" fill="none"/></svg>
      info@hollin-marsh.co.uk
    </p>
    <p class="contact__line contact__line--web">www.hollin-marsh.co.uk</p>
  </div>

  <div class="person">
    <p class="person__name"><span class="person__first">Tobias</span> <span class="person__last">Renwick</span></p>
    <p class="person__role">Managing Director</p>
  </div>
  <div class="accent-bar"></div>

  <p class="watermark">Hollin Marsh</p>
</section>

<section class="card card--back">
  <div class="back-texture" role="img" aria-label="Repeating pattern of the company emblem fading from deep grey to silver"></div>
  <div class="back-brand">
    <span class="back-brand__mark"></span>
    <span class="back-brand__name">Hollin Marsh Construction</span>
  </div>
</section>

</body>
</html>
```